Bramble Hollow is company name.Handknit&crochet blankets&scarves. Need logo&business ...

I need a design that is eye catching, using yarn and is flowing. I'd like to see colors in aqua (Halvorsen Pike paint HP4817 Merilune) for the yarn and company name. For the text, a dark grey color (Halvorsen Pike HP5308 Velden Ash)

Colors
87cfc7

```html
<!DOCTYPE html>
<html lang="en">
<head>
<meta charset="utf-8">
<title>Bramble Hollow — Business Card</title>
<link href="https://fonts.googleapis.com/css2?family=Alegreya+Sans:wght@400&display=swap" rel="stylesheet">
<style>
  :root {
    --page: #ffffff;
    --card-aqua: #89c4b6;
    --ink-white: #ffffff;
  }
  * { box-sizing: border-box; margin: 0; padding: 0; }
  html, body {
    width: 1200px;
    height: 1000px;
    overflow: hidden;
    background: var(--page);
  }
  .canvas {
    position: relative;
    width: 1200px;
    height: 1000px;
  }
  .card {
    position: absolute;
    left: 78px;
    top: 208px;
    width: 1050px;
    height: 582px;
    background: var(--card-aqua);
    font-family: "Alegreya Sans", sans-serif;
    color: var(--ink-white);
  }
  .brand {
    position: absolute;
    left: 0;
    top: 0;
    width: 640px;
    height: 582px;
  }
  .brand-name {
    position: absolute;
    left: 56px;
    top: 118px;
    font-size: 122px;
    font-weight: 400;
    line-height: 168px;
    letter-spacing: 1px;
  }
  .brand-mark {
    position: absolute;
    left: 474px;
    top: 170px;
    width: 120px;
    height: 120px;
    border-radius: 50%;
    border: 7px solid var(--ink-white);
  }
  .contact {
    position: absolute;
    right: 60px;
    top: 284px;
    text-align: right;
    font-style: normal;
    font-size: 33px;
    font-weight: 400;
    line-height: 40px;
    letter-spacing: 0.5px;
  }
  .services {
    position: absolute;
    right: 60px;
    top: 438px;
    list-style: none;
    text-align: right;
    font-size: 26px;
    font-weight: 400;
    line-height: 29px;
    letter-spacing: 1px;
    text-transform: uppercase;
  }
</style>
</head>
<body>
  <div class="canvas">
    <section class="card">
      <div class="brand">
        <h1 class="brand-name">Bramble<br>Hollow</h1>
        <span class="brand-mark" aria-hidden="true"></span>
      </div>

      <address class="contact">
        <div class="contact-name">Odette Varnum</div>
        <div class="contact-phone">phone</div>
        <div class="contact-email">email</div>
      </address>

      <ul class="services">
        <li>Hand Knit &amp; Crochet</li>
        <li>Baby Afghans &amp; Afghans</li>
        <li>Scarves, Gloves, Hat</li>
      </ul>
    </section>
  </div>
</body>
</html>
```